Design mobile friendly review and ranking site

We're working on a corporate website for reviewing and ranking fellow employees. We need the website to look both fun and professional and it needs to be responsive - to it works on mobile and desktop.

Looking for css and HTML for 3 key pages as well as a header and footer for the site. Also would need any supporting graphics as part of the design.

Target Market(s)

Professionals in their 20s, 30s, and 40s.

Industry/Entity Type

Internet

Coding

Coded - Design and coding required

Number of Pages Required

3 page

Font styles to use
Sans Serif

Requirements
Must have
• 3 key pages we need (note included screenshots for each - these are just super rough cuts so you see examples of the content.)
• a) main-intro: A compelling into page with a login/registration form. Should be sleek/modern/enticing. Also we would show the ranking for the top 3 people to tease people re: content.
• b) main-page: Has two sections: One at the top where you would rate someone and one at the bottom where it shows a ranking of people.
• c) profile page: This is where you view a specific person. You see the person's picture, some info about the person, you see their overall rating, you can rate them, and you also see their historical ratings.
Nice to have
• Note we need css and HTML for this. It should feel as sleek and modern. Note also must be responsive design so it works well in mobile and desktop.

```html
<!DOCTYPE html>
<html lang="en">
<head>
<meta charset="utf-8">
<title>Peer Tally – Rate &amp; Rank</title>
<link href="https://fonts.googleapis.com/css2?family=Open+Sans:wght@300;400&family=Roboto:wght@400;500&display=swap" rel="stylesheet">
<style>
:root{
  --ink:#222;
  --muted:#555;
  --link:#1b82c0;
  --banner-dark:#161616;
  --banner-mid:#2a2418;
  --gold:#f6c21c;
  --gold-text:#f3c614;
  --grey-star:#d3d3d3;
  --red-star:#e3202a;
  --orange-star:#ef7a1e;
  --skip:#2a9bc0;
  --save:#3d9b10;
  --band:#1b66b7;
  --field:#c9e3ee;
  --badge:#e21c1c;
  --card:#ffffff;
  --line:#d8d8d8;
}
*{box-sizing:border-box;margin:0;padding:0}
html,body{width:1041px;height:1200px;overflow:hidden}
body{position:relative;background:#fff;font-family:'Roboto',Arial,sans-serif;color:var(--ink)}
.abs{position:absolute}

/* header */
.site-header{position:absolute;left:0;top:0;width:1041px;height:72px;background:#fff}
.brand{position:absolute;left:60px;top:20px;display:flex;align-items:center;gap:8px}
.brand-dot{width:26px;height:26px;border-radius:50%;background:#2aa34a}
.brand-name{font:500 22px 'Roboto',Arial,sans-serif;color:var(--ink);letter-spacing:.2px}
.user{position:absolute;right:69px;top:15px;display:flex;align-items:center;gap:8px}
.user-name{font-size:10px;color:#777}
.user-avatar{width:42px;height:42px;border-radius:50%;background:radial-gradient(circle at 50% 40%,#8a7a6c,#2b2b2b)}

.level-banner{position:absolute;left:0;top:72px;width:1041px;height:62px;
  background:radial-gradient(ellipse at 40% 50%,#4a3a1c 0%,var(--banner-mid) 25%,var(--banner-dark) 60%)}
.level-text{position:absolute;left:68px;top:16px;font:300 21px 'Open Sans',Arial,sans-serif;color:#fff}
.share{position:absolute;right:69px;top:20px;display:flex;align-items:center;gap:7px;
  font:400 15.5px 'Open Sans',Arial,sans-serif;color:var(--gold-text)}

/* rate section */
.rate-title{position:absolute;left:70px;top:168px;font:400 23px 'Open Sans',Arial,sans-serif;color:#333;letter-spacing:.3px}
.subject-photo{position:absolute;left:70px;top:231px;width:129px;height:129px;border-radius:50%;
  border:1px solid var(--line);padding:6px;background:#fff}
.subject-photo span{display:block;width:100%;height:100%;border-radius:50%;
  background:radial-gradient(circle at 50% 45%,#c9a58a,#6e5646 70%,#3b2e26)}
.subject-name{position:absolute;left:70px;top:368px;width:129px;text-align:center;font-size:24px;font-weight:500}
.subject-link{position:absolute;left:70px;top:402px;width:129px;text-align:center;font-size:12px;font-weight:500;color:var(--link)}

.ratings{position:absolute;display:grid;grid-template-columns:auto 135px;column-gap:16px;row-gap:7px;align-items:center}
.ratings .label{text-align:right;font-size:13px;color:#444}
.rate-form .ratings{left:200px;top:255px;width:282px}
.stars{display:block;width:135px;height:24px}

.comment-label{position:absolute;left:532px;top:259px;font-size:11px;color:#444}
.comment-box{position:absolute;left:532px;top:289px;width:362px;height:108px;border:1px solid var(--line);
  font:400 11.5px 'Roboto',Arial,sans-serif;color:#aaa;padding:12px}
.btn{position:absolute;top:411px;height:32px;color:#fff;font-size:12px;font-weight:500;
  display:flex;align-items:center;justify-content:center;border-radius:2px;box-shadow:0 2px 0 rgba(0,0,0,.18)}
.btn-skip{left:532px;width:78px;background:var(--skip)}
.btn-save{left:625px;width:79px;background:var(--save)}

/* ranking */
.filter-band{position:absolute;left:0;top:517px;width:1041px;height:56px;background:var(--band)}
.filter-zig{position:absolute;left:0;top:572px;width:1041px;height:6px}
.select{position:absolute;top:527px;height:35px;background:#fff;display:flex;align-items:center;
  justify-content:space-between;padding:0 12px 0 17px;font-size:16px;color:#333}
.join-word{position:absolute;top:533px;font-size:19px;color:#fff}
.ranking-bg{position:absolute;left:0;top:573px;width:1041px;height:627px;background:var(--field)}

.rank-card{position:absolute;left:69px;width:902px;height:176px;background:var(--card);box-shadow:0 1px 3px rgba(0,0,0,.12)}
.rank-photo{position:absolute;left:42px;top:18px;width:129px;height:129px;border-radius:50%;border:1px solid var(--line);padding:7px;background:#fff}
.rank-photo span{display:block;width:100%;height:100%;border-radius:50%}
.badge{position:absolute;left:186px;top:32px;height:26px;padding:0 8px;background:var(--badge);color:#fff;
  font-size:13.5px;display:flex;align-items:center}
.rank-name{position:absolute;left:185px;top:64px;font-size:23px;font-weight:500}
.rank-points{position:absolute;left:185px;top:103px;font-size:15px;font-weight:500;color:#333}
.rank-reviews{position:absolute;left:185px;top:125px;font-size:11.5px;color:#555}
.rank-reviews b{color:var(--link);font-weight:500}
.rank-card .ratings{right:46px;top:44px;row-gap:7px}
</style>
</head>
<body>

<svg width="0" height="0" style="position:absolute" aria-hidden="true">
  <defs>
    <symbol id="star" viewBox="0 0 24 24"><path d="M12 1.5l3.1 7.2 7.8.7-5.9 5.1 1.8 7.6L12 18l-6.8 4.1 1.8-7.6-5.9-5.1 7.8-.7z"/></symbol>
  </defs>
</svg>

<header class="site-header">
  <div class="brand"><span class="brand-dot"></span><span class="brand-name">PEER TALLY</span></div>
  <div class="user"><span class="user-name">Alex Carter</span><span class="user-avatar" role="img" aria-label="Profile photo of the signed-in user"></span></div>
</header>

<div class="level-banner">
  <div class="level-text">Lavel 3 - 41 points to level 4</div>
  <div class="share">
    <svg width="21" height="21" viewBox="0 0 21 21" fill="none" stroke="currentColor" stroke-width="1.6">
      <rect x="1" y="1" width="19" height="19"/><line x1="1" y1="4.5" x2="20" y2="4.5"/>
      <circle cx="14" cy="8.5" r="1.4"/><circle cx="7" cy="12" r="1.4"/><circle cx="14" cy="15.5" r="1.4"/>
      <line x1="12.6" y1="9.2" x2="8.3" y2="11.3"/><line x1="8.3" y1="12.7" x2="12.6" y2="14.8"/>
    </svg>
    Share this to get more points!
  </div>
</div>

<section class="rate-form">
  <h1 class="rate-title">Anonymously rate this person for a point :</h1>
  <div class="subject-photo"><span role="img" aria-label="Portrait photo of the person being rated"></span></div>
  <div class="subject-name">Daniel</div>
  <div class="subject-link">View Reviews</div>

  <div class="ratings">
    <span class="label">Smarts</span>
    <svg class="stars" viewBox="0 0 135 24"><use href="#star" x="0" width="24" height="24" fill="var(--gold)"/><use href="#star" x="27.5" width="24" height="24" fill="var(--gold)"/><use href="#star" x="55" width="24" height="24" fill="var(--gold)"/><use href="#star" x="82.5" width="24" height="24" fill="var(--grey-star)"/><use href="#star" x="110" width="24" height="24" fill="var(--grey-star)"/></svg>
    <span class="label">Easy To Work With</span>
    <svg class="stars" viewBox="0 0 135 24"><use href="#star" x="0" width="24" height="24" fill="var(--gold)"/><use href="#star" x="27.5" width="24" height="24" fill="var(--gold)"/><use href="#star" x="55" width="24" height="24" fill="var(--gold)"/><use href="#star" x="82.5" width="24" height="24" fill="var(--gold)"/><use href="#star" x="110" width="24" height="24" fill="var(--gold)"/></svg>
    <span class="label">Hard Worker</span>
    <svg class="stars" viewBox="0 0 135 24"><use href="#star" x="0" width="24" height="24" fill="var(--gold)"/><use href="#star" x="27.5" width="24" height="24" fill="var(--gold)"/><use href="#star" x="55" width="24" height="24" fill="var(--gold)"/><use href="#star" x="82.5" width="24" height="24" fill="var(--gold)"/><use href="#star" x="110" width="24" height="24" fill="var(--grey-star)"/></svg>
  </div>

  <div class="comment-label">(Optional) Write an an anonymous comment about this persopn :</div>
  <div class="comment-box">Enter your Keywords</div>
  <div class="btn btn-skip">SKIP</div>
  <div class="btn btn-save">SAVE</div>
</section>

<div class="ranking-bg"></div>
<div class="filter-band"></div>
<svg class="filter-zig" viewBox="0 0 1041 6" preserveAspectRatio="none"><path fill="var(--band)" d="M0 0H1041V0L1035 6 1029 0 1023 6 1017 0 1011 6 1005 0 999 6 993 0 987 6 981 0 975 6 969 0 963 6 957 0 951 6 945 0 939 6 933 0 927 6 921 0 915 6 909 0 903 6 897 0 891 6 885 0 879 6 873 0 867 6 861 0 855 6 849 0 843 6 837 0 831 6 825 0 819 6 813 0 807 6 801 0 795 6 789 0 783 6 777 0 771 6 765 0 759 6 753 0 747 6 741 0 735 6 729 0 723 6 717 0 711 6 705 0 699 6 693 0 687 6 681 0 675 6 669 0 663 6 657 0 651 6 645 0 639 6 633 0 627 6 621 0 615 6 609 0 603 6 597 0 591 6 585 0 579 6 573 0 567 6 561 0 555 6 549 0 543 6 537 0 531 6 525 0 519 6 513 0 507 6 501 0 495 6 489 0 483 6 477 0 471 6 465 0 459 6 453 0 447 6 441 0 435 6 429 0 423 6 417 0 411 6 405 0 399 6 393 0 387 6 381 0 375 6 369 0 363 6 357 0 351 6 345 0 339 6 333 0 327 6 321 0 315 6 309 0 303 6 297 0 291 6 285 0 279 6 273 0 267 6 261 0 255 6 249 0 243 6 237 0 231 6 225 0 219 6 213 0 207 6 201 0 195 6 189 0 183 6 177 0 171 6 165 0 159 6 153 0 147 6 141 0 135 6 129 0 123 6 117 0 111 6 105 0 99 6 93 0 87 6 81 0 75 6 69 0 63 6 57 0 51 6 45 0 39 6 33 0 27 6 21 0 15 6 9 0 3 6 0 0Z"/></svg>

<div class="select" style="left:70px;width:129px">Best <svg width="12" height="8" viewBox="0 0 12 8"><path d="M1 1l5 5 5-5" fill="none" stroke="#555" stroke-width="1.5"/></svg></div>
<span class="join-word" style="left:220px">in</span>
<div class="select" style="left:255px;width:276px">All Functions <svg width="12" height="8" viewBox="0 0 12 8"><path d="M1 1l5 5 5-5" fill="none" stroke="#555" stroke-width="1.5"/></svg></div>
<span class="join-word" style="left:548px">and</span>
<div class="select" style="left:596px;width:276px">All Levels <svg width="12" height="8" viewBox="0 0 12 8"><path d="M1 1l5 5 5-5" fill="none" stroke="#555" stroke-width="1.5"/></svg></div>

<article class="rank-card" style="top:594px">
  <div class="rank-photo"><span role="img" aria-label="Portrait photo of ranked colleague" style="background:radial-gradient(circle at 50% 40%,#d9b8a0,#8c8a86 60%,#2a2f3a)"></span></div>
  <div class="badge">#1 worst</div>
  <div class="rank-name">Greg Holden</div>
  <div class="rank-points">Point: 15</div>
  <div class="rank-reviews">Number Of Reviews: <b>1 View Details</b></div>
  <div class="ratings">
    <span class="label">Smarts</span>
    <svg class="stars" viewBox="0 0 135 24"><use href="#star" x="0" width="24" height="24" fill="var(--gold)"/><use href="#star" x="27.5" width="24" height="24" fill="var(--gold)"/><use href="#star" x="55" width="24" height="24" fill="var(--gold)"/><use href="#star" x="82.5" width="24" height="24" fill="var(--grey-star)"/><use href="#star" x="110" width="24" height="24" fill="var(--grey-star)"/></svg>
    <span class="label">Easy To Work With</span>
    <svg class="stars" viewBox="0 0 135 24"><use href="#star" x="0" width="24" height="24" fill="var(--gold)"/><use href="#star" x="27.5" width="24" height="24" fill="var(--gold)"/><use href="#star" x="55" width="24" height="24" fill="var(--gold)"/><use href="#star" x="82.5" width="24" height="24" fill="var(--gold)"/><use href="#star" x="110" width="24" height="24" fill="var(--gold)"/></svg>
    <span class="label">Hard Worker</span>
    <svg class="stars" viewBox="0 0 135 24"><use href="#star" x="0" width="24" height="24" fill="var(--gold)"/><use href="#star" x="27.5" width="24" height="24" fill="var(--gold)"/><use href="#star" x="55" width="24" height="24" fill="var(--gold)"/><use href="#star" x="82.5" width="24" height="24" fill="var(--gold)"/><use href="#star" x="110" width="24" height="24" fill="var(--grey-star)"/></svg>
  </div>
</article>

<article class="rank-card" style="top:778px">
  <div class="rank-photo"><span role="img" aria-label="Portrait photo of ranked colleague" style="background:radial-gradient(circle at 50% 40%,#e0b9a0,#8a5a3e 55%,#1d1d24)"></span></div>
  <div class="badge">#2 worst</div>
  <div class="rank-name">Laura Benton</div>
  <div class="rank-points">Point: 15</div>
  <div class="rank-reviews">Number Of Reviews: <b>2 View Details</b></div>
  <div class="ratings">
    <span class="label">Smarts</span>
    <svg class="stars" viewBox="0 0 135 24"><use href="#star" x="0" width="24" height="24" fill="var(--red-star)"/><use href="#star" x="27.5" width="24" height="24" fill="var(--grey-star)"/><use href="#star" x="55" width="24" height="24" fill="var(--grey-star)"/><use href="#star" x="82.5" width="24" height="24" fill="var(--grey-star)"/><use href="#star" x="110" width="24" height="24" fill="var(--grey-star)"/></svg>
    <span class="label">Easy To Work With</span>
    <svg class="stars" viewBox="0 0 135 24"><use href="#star" x="0" width="24" height="24" fill="var(--orange-star)"/><use href="#star" x="27.5" width="24" height="24" fill="var(--orange-star)"/><use href="#star" x="55" width="24" height="24" fill="var(--orange-star)"/><use href="#star" x="82.5" width="24" height="24" fill="var(--grey-star)"/><use href="#star" x="110" width="24" height="24" fill="var(--grey-star)"/></svg>
    <span class="label">Hard Worker</span>
    <svg class="stars" viewBox="0 0 135 24"><use href="#star" x="0" width="24" height="24" fill="var(--gold)"/><use href="#star" x="27.5" width="24" height="24" fill="var(--gold)"/><use href="#star" x="55" width="24" height="24" fill="var(--gold)"/><use href="#star" x="82.5" width="24" height="24" fill="var(--gold)"/><use href="#star" x="110" width="24" height="24" fill="var(--grey-star)"/></svg>
  </div>
</article>

<article class="rank-card" style="top:962px">
  <div class="rank-photo"><span role="img" aria-label="Portrait photo of ranked colleague" style="background:radial-gradient(circle at 50% 40%,#c8a088,#5c4a40 55%,#222)"></span></div>
  <div class="badge">#3 worst</div>
  <div class="rank-name">Ryan Mercer</div>
  <div class="rank-points">Point: 15</div>
  <div class="rank-reviews">Number Of Reviews: <b>2 View Details</b></div>
  <div class="ratings">
    <span class="label">Smarts</span>
    <svg class="stars" viewBox="0 0 135 24"><use href="#star" x="0" width="24" height="24" fill="var(--red-star)"/><use href="#star" x="27.5" width="24" height="24" fill="var(--grey-star)"/><use href="#star" x="55" width="24" height="24" fill="var(--grey-star)"/><use href="#star" x="82.5" width="24" height="24" fill="var(--grey-star)"/><use href="#star" x="110" width="24" height="24" fill="var(--grey-star)"/></svg>
    <span class="label">Easy To Work With</span>
    <svg class="stars" viewBox="0 0 135 24"><use href="#star" x="0" width="24" height="24" fill="var(--orange-star)"/><use href="#star" x="27.5" width="24" height="24" fill="var(--grey-star)"/><use href="#star" x="55" width="24" height="24" fill="var(--grey-star)"/><use href="#star" x="82.5" width="24" height="24" fill="var(--grey-star)"/><use href="#star" x="110" width="24" height="24" fill="var(--grey-star)"/></svg>
    <span class="label">Hard Worker</span>
    <svg class="stars" viewBox="0 0 135 24"><use href="#star" x="0" width="24" height="24" fill="var(--gold)"/><use href="#star" x="27.5" width="24" height="24" fill="var(--gold)"/><use href="#star" x="55" width="24" height="24" fill="var(--gold)"/><use href="#star" x="82.5" width="24" height="24" fill="var(--gold)"/><use href="#star" x="110" width="24" height="24" fill="var(--gold)"/></svg>
  </div>
</article>

</body>
</html>
```